Sales Flyer for Outdoor Kitchens

Looks to have a trifold flyer designed based off website content / projects. Use www.patiohearthcrafters.com for content

```html
<!DOCTYPE html>
<html lang="en">
<head>
<meta charset="utf-8">
<title>Patio Hearth Crafters – Trifold Flyer</title>
<link href="https://fonts.googleapis.com/css2?family=Montserrat:wght@600;700;800;900&family=Open+Sans:wght@400;600;700&display=swap" rel="stylesheet">
<style>
:root{
  --navy:#0e2a47;
  --green:#3aa935;
  --green-dark:#23802a;
  --blue:#1f72b8;
  --sky:#dbe8f3;
  --page:#e8eef4;
  --white:#ffffff;
  --text:#33414f;
  --wood-a:#8a5a34;
  --wood-b:#c79a6a;
  --stone-a:#6e7379;
  --stone-b:#b9b3a8;
}
*{box-sizing:border-box;margin:0;padding:0}
html,body{width:1200px;height:2524px;overflow:hidden}
body{background:var(--page);font-family:"Open Sans",Arial,sans-serif;color:var(--text);position:relative}
.spread{position:absolute;left:40px;width:1120px;height:865px;background:var(--white);display:flex;box-shadow:0 10px 30px rgba(14,42,71,.18)}
.spread--outside{top:297px}
.spread--inside{top:1362px}
.panel{width:373.33px;height:100%;position:relative;display:flex;flex-direction:column;overflow:hidden}
.panel + .panel{border-left:1px solid #e3e8ee}
.photo{width:100%;flex:none}
.photo--wood{background:linear-gradient(160deg,var(--wood-a),var(--wood-b) 55%,#5c7a4a)}
.photo--stone{background:linear-gradient(160deg,var(--stone-a),var(--stone-b) 60%,#7d8f6a)}
.photo--room{background:linear-gradient(160deg,#6b4a33,#d8c3a4 55%,#9aa7b0)}
.heading{font-family:Montserrat,Arial,sans-serif;font-weight:800;font-size:24px;color:var(--navy);letter-spacing:.5px;text-transform:uppercase}
.heading::after{content:"";display:block;width:56px;height:4px;background:var(--green);margin-top:8px;border-radius:2px}
.body-copy{font-size:12.5px;line-height:1.6}
.body-copy p{margin-top:10px}
.body-copy b{color:var(--green-dark)}
.pad{padding:30px 30px 0}
.pad--after-wave{padding-top:40px}
.swoosh{position:absolute;left:0;width:100%;height:60px;z-index:0}
/* brand */
.brand{display:flex;align-items:center;gap:10px;font-family:Montserrat,Arial,sans-serif;font-weight:800;color:var(--navy);text-transform:uppercase}
.brand__dot{width:18px;height:18px;border-radius:50%;background:var(--green);flex:none}
/* back panel */
.quote{background:var(--sky);border-left:4px solid var(--green);padding:12px 14px;margin-top:14px;font-size:12px;line-height:1.55;font-style:italic}
.quote cite{display:block;margin-top:6px;font-style:normal;font-weight:700;color:var(--navy);font-size:11.5px}
.contact{background:var(--navy);color:var(--white);margin-top:auto;padding:20px 30px;font-size:13px}
.contact li{list-style:none;display:flex;align-items:center;gap:10px;margin:6px 0}
.contact svg{width:18px;height:18px;flex:none}
/* cover */
.cover__brand{padding:40px 30px 0;font-size:18px}
.cover__title{font-family:Montserrat,Arial,sans-serif;font-weight:900;font-size:36px;line-height:1.08;color:var(--navy);padding:16px 30px 0;text-transform:uppercase}
.cover__title span{color:var(--green)}
.phone-band{margin:20px 0 0;background:var(--blue);color:var(--white);font-family:Montserrat,Arial,sans-serif;font-weight:800;font-size:28px;padding:12px 30px;display:flex;align-items:center;gap:12px}
.phone-band svg{width:26px;height:26px}
.cover__web{padding:12px 30px;font-weight:700;color:var(--navy);font-size:14px}
/* inside */
.bullets{list-style:none;margin-top:14px}
.bullets li{position:relative;padding-left:18px;margin-bottom:10px;font-size:12.5px;line-height:1.55}
.bullets li::before{content:"";position:absolute;left:0;top:6px;width:9px;height:9px;border-radius:50%;background:var(--green)}
.bullets b{color:var(--green-dark)}
.panel--green{background:var(--green-dark);color:var(--white);align-items:center;padding-top:30px}
.panel--green .heading{color:var(--white);text-align:center}
.panel--green .heading::after{background:var(--white);margin:8px auto 0}
.sub{font-family:Montserrat,Arial,sans-serif;font-weight:700;font-size:14px;margin-top:14px;text-transform:uppercase}
.sub small{display:block;font-family:"Open Sans",Arial,sans-serif;font-weight:400;font-size:11px;text-transform:none;text-align:center;opacity:.9}
.service{width:300px;margin-top:12px;height:108px;position:relative;border:3px solid var(--white);border-radius:6px;overflow:hidden}
.service__label{position:absolute;left:0;right:0;bottom:0;background:var(--navy);color:var(--white);font-family:Montserrat,Arial,sans-serif;font-weight:700;font-size:12px;text-align:center;padding:5px 0;text-transform:uppercase}
.service:nth-child(odd) .service__label{background:var(--green)}
</style>
</head>
<body>

<section class="spread spread--outside">
  <article class="panel">
    <div class="pad">
      <h2 class="heading">About Us</h2>
      <div class="body-copy">
        <p><b>Patio Hearth Crafters</b> designs and builds complete outdoor living spaces, from the first sketch to the final stone, so every backyard feels like a true extension of your home.</p>
        <p>Our team blends craftsmanship with practical planning, creating kitchens, patios and fire features that are built to last and made for gathering with family and friends.</p>
        <p>We handle every detail in one place, keeping your project simple, on schedule and stress free from start to finish.</p>
      </div>
    </div>
    <div class="photo photo--stone" style="margin-top:auto;height:300px" role="img" aria-label="Photo of a finished outdoor kitchen with stone counters"></div>
  </article>

  <article class="panel">
    <div class="pad">
      <h2 class="heading">Testimonials</h2>
      <div class="quote">“They turned our empty yard into our favorite room. The kitchen and fire pit are perfect for weekend dinners.”<cite>— Client, Katy</cite></div>
      <div class="quote">“Clear pricing, great crew and beautiful work. Our patio was finished right on time.”<cite>— Client, Cypress</cite></div>
      <div class="brand" style="margin-top:30px;font-size:20px;justify-content:center"><span class="brand__dot"></span>Patio Hearth Crafters</div>
    </div>
    <ul class="contact">
      <li><svg viewBox="0 0 24 24" fill="#3aa935"><path d="M6.6 10.8a15 15 0 0 0 6.6 6.6l2.2-2.2a1 1 0 0 1 1-.25 11.4 11.4 0 0 0 3.6.57 1 1 0 0 1 1 1V20a1 1 0 0 1-1 1A17 17 0 0 1 3 4a1 1 0 0 1 1-1h3.5a1 1 0 0 1 1 1c0 1.25.2 2.45.57 3.6a1 1 0 0 1-.25 1z"/></svg>281-555-0186</li>
      <li><svg viewBox="0 0 24 24" fill="#3aa935"><circle cx="12" cy="12" r="10"/><path d="M2 12h20M12 2c3 3 3 17 0 20M12 2c-3 3-3 17 0 20" stroke="#0e2a47" stroke-width="1.5" fill="none"/></svg>www.patiohearthcrafters.com</li>
      <li><svg viewBox="0 0 24 24" fill="#3aa935"><path d="M12 2a7 7 0 0 0-7 7c0 5 7 13 7 13s7-8 7-13a7 7 0 0 0-7-7zm0 9.5A2.5 2.5 0 1 1 12 6.5a2.5 2.5 0 0 1 0 5z"/></svg>Serving Greater Houston, TX</li>
    </ul>
  </article>

  <article class="panel">
    <div class="photo photo--wood" style="height:380px" role="img" aria-label="Photo of a covered timber pavilion with outdoor seating"></div>
    <svg class="swoosh" style="top:340px" viewBox="0 0 373 60" preserveAspectRatio="none"><path d="M0 30 Q190 0 373 20 V60 H0Z" fill="#3aa935"/><path d="M0 40 Q190 14 373 30 V60 H0Z" fill="#fff"/></svg>
    <div class="brand cover__brand"><span class="brand__dot"></span>Patio Hearth Crafters</div>
    <h1 class="cover__title">Create <span>your dream</span> backyard with us</h1>
    <div class="phone-band"><svg viewBox="0 0 24 24" fill="#fff"><path d="M6.6 10.8a15 15 0 0 0 6.6 6.6l2.2-2.2a1 1 0 0 1 1-.25 11.4 11.4 0 0 0 3.6.57 1 1 0 0 1 1 1V20a1 1 0 0 1-1 1A17 17 0 0 1 3 4a1 1 0 0 1 1-1h3.5a1 1 0 0 1 1 1c0 1.25.2 2.45.57 3.6a1 1 0 0 1-.25 1z"/></svg>281-555-0186</div>
    <p class="cover__web">www.patiohearthcrafters.com</p>
  </article>
</section>

<section class="spread spread--inside">
  <article class="panel">
    <div class="pad">
      <h2 class="heading">Our Expertise</h2>
      <ul class="bullets">
        <li><b>Outdoor Living Areas:</b> full backyard plans that balance cooking, dining and lounging zones for the way your family lives.</li>
        <li><b>Custom Kitchens:</b> grills, smokers, pizza ovens and storage built into durable counters made for the Texas weather.</li>
        <li><b>Shade Structures:</b> pergolas and pavilions that add comfort, style and year round use to any patio.</li>
        <li><b>Fire Features:</b> fireplaces and fire pits designed as the warm centerpiece of your evening gatherings.</li>
      </ul>
    </div>
    <div class="photo photo--stone" style="margin-top:auto;height:250px" role="img" aria-label="Photo of a stone outdoor grill station"></div>
  </article>

  <article class="panel panel--green">
    <h2 class="heading">What We Do</h2>
    <p class="sub">Our Turnkey Services<small>We deliver complete outdoor spaces</small></p>
    <div>
      <div class="service photo--stone" role="img" aria-label="Photo of an outdoor kitchen"><span class="service__label">Outdoor Kitchens</span></div>
      <div class="service photo--wood" role="img" aria-label="Photo of a patio with pergola"><span class="service__label">Fireplaces, Patios &amp; Pergolas</span></div>
      <div class="service photo--room" role="img" aria-label="Photo of a fire pit"><span class="service__label">Fire Pits</span></div>
      <div class="service" style="background:linear-gradient(160deg,#2d7fb8,#8fd0e6)" role="img" aria-label="Photo of a backyard pool"><span class="service__label">Pools</span></div>
      <div class="service" style="background:linear-gradient(160deg,#3f6a35,#a5c27c)" role="img" aria-label="Photo of lit garden landscaping"><span class="service__label">Landscaping &amp; Lighting</span></div>
    </div>
  </article>

  <article class="panel">
    <div class="photo photo--room" style="height:330px" role="img" aria-label="Photo of a covered patio with fireplace and mounted television"></div>
    <svg class="swoosh" style="top:290px" viewBox="0 0 373 60" preserveAspectRatio="none"><path d="M0 20 Q190 0 373 30 V60 H0Z" fill="#1f72b8"/><path d="M0 32 Q190 12 373 42 V60 H0Z" fill="#fff"/></svg>
    <div class="pad pad--after-wave">
      <h2 class="heading">Our Values</h2>
      <ul class="bullets">
        <li><b>Quality:</b> we use proven materials and careful building methods so your space looks great for years.</li>
        <li><b>Attention to Detail:</b> every joint, finish and fixture is checked so the whole design feels complete.</li>
        <li><b>Client Centered:</b> we listen first, share clear options and keep you informed at every stage of the build.</li>
      </ul>
    </div>
  </article>
</section>

</body>
</html>
```